Letterhead design for Sleep Consulting Business

I'm looking for a new letterhead (heading/footer) design for my Sleep Consulting Business, I work with families to help their children improve their sleep.

The heading/footer will used in Microsoft Word Only-to be used for all of my documents such as writing Sleep Plans. I need to utilize as much working space in the document as possible. This will NOT be printed out on paper- it will only be used for heading/footer on microsoft word, then emailed to clients, who may print it at home.

My brand colors:
Dark Blue Hex: 1F2A42
Lighter Blueish Hex: 90BEC9
You're welcome to check out my website for inspiration- it is freshly created with other colors as well, and I love the outcome. www.hollowpinerest.com

Target Market(s)

Tired parents

Font styles to use
Script
Other font styles liked:
• Great Vibe, Lato or Just Another Hand are all used currently for my brand. Open to other options.

Requirements
Must have
• The letterhead (heading/footer) MUST be kept narrow (height-wise), so I have plenty of space on my document, while including important information.

It should look professional on screen, and when printed.

Must include my business name OR logo (Hollow Pine Sleep Consulting), and my email address. Mara@hollowpinerest.com

Website is optional, not required, just if you need to fill in a spot: www.hollowpinerest.com

```html
<!DOCTYPE html>
<html lang="en">
<head>
<meta charset="utf-8">
<title>Hollow Pine Sleep Consulting – Letterhead</title>
<link rel="stylesheet" href="https://fonts.googleapis.com/css2?family=Open+Sans:wght@400;600&family=Lato:wght@400;700&display=swap">
<style>
  :root {
    --navy: #1F2A42;
    --sky: #90BEC9;
    --ink: #3a3a3a;
    --rule: #c9ccd2;
    --paper: #ffffff;
    --sig: #d9dde3;
  }
  * { margin: 0; padding: 0; box-sizing: border-box; }
  html, body { width: 1040px; height: 1200px; overflow: hidden; background: var(--paper); }
  .letterhead {
    position: relative;
    width: 1040px;
    height: 1200px;
    background: var(--paper);
    font-family: "Open Sans", Arial, sans-serif;
    color: var(--ink);
  }
  .side-bar {
    position: absolute;
    left: 23px; top: 0;
    width: 8px; height: 1012px;
    background: var(--sky);
  }
  .corner-star {
    position: absolute;
    left: 0; top: 1000px;
    width: 150px; height: 200px;
  }
  .brand {
    position: absolute;
    top: 40px; left: 0; right: 0;
    display: flex; align-items: center; justify-content: center; gap: 14px;
  }
  .brand-dot {
    width: 44px; height: 44px; border-radius: 50%;
    background: var(--sky);
  }
  .brand-name {
    font-family: "Lato", Arial, sans-serif;
    font-weight: 400;
    font-size: 30px;
    color: var(--navy);
    letter-spacing: 0.5px;
  }
  .letter {
    position: absolute;
    left: 99px; top: 224px;
    width: 841px;
    font-size: 15px;
    line-height: 18px;
  }
  .issue-date { margin-bottom: 19px; }
  .recipient { margin-bottom: 48px; }
  .salutation { margin-bottom: 30px; }
  .body-copy p {
    text-align: justify;
    line-height: 27px;
    margin-bottom: 27px;
  }
  .closing { margin-top: 40px; }
  .signature {
    width: 215px; height: 22px;
    margin: 16px 0 14px;
    background: linear-gradient(90deg, var(--sig), #eef0f3);
    border-radius: 11px;
  }
  .signer-name { font-size: 19px; font-weight: 600; color: #2b2b2b; line-height: 24px; }
  .signer-role { margin-top: 6px; }
  .footer {
    position: absolute;
    left: 207px; width: 627px; top: 1140px;
    display: flex; align-items: center; gap: 12px;
  }
  .footer-rule { flex: 1; height: 1px; background: var(--rule); }
  .footer-email {
    font-family: "Lato", Arial, sans-serif;
    font-size: 18px;
    color: #222;
    white-space: nowrap;
  }
  .footer-email b { font-weight: 700; }
</style>
</head>
<body>
<div class="letterhead">
  <div class="side-bar"></div>
  <svg class="corner-star" viewBox="0 0 150 200" aria-hidden="true">
    <polygon fill="#90BEC9" points="31,0 54,68 143,68 86,120 100,200 31,160 -40,200 -26,120 -83,68 8,68"/>
  </svg>

  <header class="brand">
    <span class="brand-dot"></span>
    <span class="brand-name">Hollow Pine Sleep Consulting</span>
  </header>

  <main class="letter">
    <p class="issue-date">Issuing Date: May 5, 2018</p>
    <p class="recipient">Name Of Employee Mr. XYZABC<br>Address of Employee<br>Address Line 2 etc..</p>
    <p class="salutation">Dear Mr.XYZABC</p>
    <div class="body-copy">
      <p>Lorem Ipsum has been the industry's standard dummy text ever since the 1500s, when an unknown printer took a galley of type and scrambled it to make a type specimen book. It has survived not only five centuries, but also the leap into electronic typesetting, remaining essentially unchanged. It was popularised in the 1960s with the release of Typeline sheets containing Lorem Ipsum passages, and more recently with desktop publishing software like Pagecraft Studio including versions of Lorem Ipsum.</p>
      <p>Lorem Ipsum is simply dummy text of the printing and typesetting industry. Lorem Ipsum has been the industry's standard dummy text ever since the 1500s, when an unknown printer took a galley of type and scrambled it to make a type specimen book.</p>
      <p>It has survived not only five centuries, but also the leap into electronic typesetting, remaining essentially unchanged. It was popularised in the 1960s with the release of Typeline sheets containing Lorem IpsumIpsum passages.</p>
    </div>
    <div class="closing">
      <p>Yours Sincerely</p>
      <div class="signature" role="img" aria-label="Handwritten signature of Daniel Reyes"></div>
      <p class="signer-name">Daniel Reyes</p>
      <p class="signer-role">Managing Director</p>
    </div>
  </main>

  <footer class="footer">
    <span class="footer-rule"></span>
    <span class="footer-email"><b>E:</b> Mara@hollowpinerest.com</span>
    <span class="footer-rule"></span>
  </footer>
</div>
</body>
</html>
```